Keen Volt Electrical in need of a business card design

We need a new business card designed for our electrical business. We have a logo already which I will attach below.
Would like the business card to be..
-BLACK background preferably, possibly white back ground behind logo if colours clash.
-White & Blue (logo blue) text
Something that makes the logo pop, & a modern look. Possibly minimal clean format.

REQUIRE:
-Logo on front & back

TEXT TO INCLUDE (ON ONE SIDE):

Tom Harlow
Director/Electrician
M: 0412 563 718
E:info@keenvoltelectrical.com.au
W:www.keenvoltelectrical.com.au
R.E.C 58431

Custom/New Homes
Renovations
Commercial Office/Shop Fit-outs
Communications & Security Cameras
Electric Vehicle Chargers
Airconditioning
Updates

Requirements
Nice to have
• Possibly even lighten the grey shades for the words 'Keen' & 'Volt' to be more easily read on a black background.

```html
<!DOCTYPE html>
<html lang="en">
<head>
<meta charset="utf-8">
<title>Keen Volt Electrical — Business Card</title>
<link rel="stylesheet" href="https://fonts.googleapis.com/css2?family=Montserrat:wght@400;500;600&display=swap">
<style>
  :root {
    --backdrop: #4a4a4a;
    --card: #0a0a0a;
    --blue: #00a6e2;
    --white: #ffffff;
    --panel: #ffffff;
  }
  * { box-sizing: border-box; margin: 0; padding: 0; }
  html, body {
    width: 1200px; height: 1200px; overflow: hidden;
    background: var(--backdrop);
    font-family: "Montserrat", "Century Gothic", sans-serif;
    color: var(--white);
  }
  .stage {
    width: 1200px; height: 1200px;
    display: flex; flex-direction: column; align-items: center; justify-content: center;
    gap: 56px;
  }
  .card {
    position: relative;
    width: 860px; height: 491px;
    background: var(--card);
    overflow: hidden;
    box-shadow: 0 10px 30px rgba(0,0,0,.35);
  }
  .brand { display: flex; align-items: center; gap: 14px; }
  .brand-mark { width: 26px; height: 26px; background: var(--blue); flex: none; }
  .brand-name { font-weight: 600; color: var(--white); letter-spacing: .5px; white-space: nowrap; }

  /* front */
  .card-front .brand { position: absolute; left: 250px; top: 170px; }
  .card-front .brand-name { font-size: 44px; }
  .card-front .brand-mark { width: 40px; height: 40px; }
  .services {
    position: absolute; left: 0; right: 0; top: 372px;
    text-align: center; font-size: 19px; line-height: 1.55; font-weight: 400;
  }
  .services .sep { color: var(--blue); margin: 0 6px; }

  /* back */
  .card-back .brand { position: absolute; left: 60px; top: 118px; }
  .card-back .brand-name { font-size: 30px; }
  .divider {
    position: absolute; left: 430px; top: 90px; width: 1px; height: 200px;
    background: var(--white);
  }
  .contact { position: absolute; left: 470px; top: 100px; }
  .contact-name { font-size: 36px; font-weight: 600; color: var(--blue); line-height: 1.1; }
  .contact-role { font-size: 19px; margin-top: 4px; }
  .contact-list { list-style: none; margin-top: 26px; font-size: 19px; line-height: 1.7; }
  .contact-list li { display: flex; align-items: center; gap: 10px; }
  .contact-list svg { width: 16px; height: 16px; flex: none; }
  .footer-art { position: absolute; left: 0; bottom: 0; width: 860px; height: 70px; }
  .licence {
    position: absolute; right: 60px; bottom: 12px;
    font-size: 24px; font-weight: 500; color: var(--blue);
  }
</style>
</head>
<body>
<main class="stage">
  <section class="card card-front" aria-label="Card front">
    <div class="brand">
      <span class="brand-mark"></span>
      <span class="brand-name">Keen Volt Electrical</span>
    </div>
    <p class="services">
      Custom/New Homes<span class="sep">/</span>Renovations<span class="sep">/</span>Commercial Office/Shop Fit-outs<br>
      Communications &amp; Security Cameras<span class="sep">/</span>Electric Vehicle Chargers<span class="sep">/</span>Airconditioning
    </p>
  </section>

  <section class="card card-back" aria-label="Card back">
    <div class="brand">
      <span class="brand-mark"></span>
      <span class="brand-name">Keen Volt Electrical</span>
    </div>
    <div class="divider"></div>
    <div class="contact">
      <p class="contact-name">Tom Harlow</p>
      <p class="contact-role">Director/Electrician</p>
      <ul class="contact-list">
        <li>
          <svg viewBox="0 0 16 16" aria-hidden="true"><rect x="4" y="1" width="8" height="14" rx="1.5" fill="none" stroke="var(--blue)" stroke-width="1.5"/></svg>
          0412 563 718
        </li>
        <li>
          <svg viewBox="0 0 16 16" aria-hidden="true"><rect x="1" y="3" width="14" height="10" fill="var(--blue)"/><path d="M1 3l7 6 7-6" fill="none" stroke="var(--card)" stroke-width="1.2"/></svg>
          info@keenvoltelectrical.com.au
        </li>
        <li>
          <svg viewBox="0 0 16 16" aria-hidden="true"><g fill="none" stroke="var(--blue)" stroke-width="1.2"><circle cx="8" cy="8" r="6.5"/><ellipse cx="8" cy="8" rx="3" ry="6.5"/><path d="M1.5 8h13M3 4.5h10M3 11.5h10"/></g></svg>
          www.keenvoltelectrical.com.au
        </li>
      </ul>
    </div>
    <svg class="footer-art" viewBox="0 0 860 70" preserveAspectRatio="none" aria-hidden="true">
      <polygon points="0,52 560,52 545,70 0,70" fill="var(--blue)"/>
      <polygon points="600,20 860,20 860,70 548,70" fill="var(--panel)"/>
    </svg>
    <p class="licence">R.E.C 58431</p>
  </section>
</main>
</body>
</html>
```